Business card - Brio Margin - size 85 mm * 55 mm

We need new business cards. Design must fit with our vision of the firm. You find in the attached file our logo and a short description of our firm (mission, vision, value, business and so on).

Target Market(s)

Consulting firm in performance improvement

Industry/Entity Type

Management Consulting

Contact Information for Business Card

SIZE
85 mm * 55 mm
INFORMATIONS
name surname
role position
telephone number
email address

Requirements
Must have
• the brand must APPEAR for the rest Would we like to have something sleek, inspired to a "just right" approach
Should not have
• Please avoid the black color as background

```html
<!DOCTYPE html>
<html lang="en">
<head>
<meta charset="utf-8">
<title>Brio Margin – Business Card</title>
<link rel="stylesheet" href="https://fonts.googleapis.com/css2?family=Questrial&display=swap">
<style>
  :root {
    --stage: #3b3b3b;
    --card: #444444;
    --lime: #8dc63f;
    --ink-light: #f2f2f2;
    --shadow: rgba(0, 0, 0, 0.35);
  }
  * { box-sizing: border-box; margin: 0; padding: 0; }
  html, body {
    width: 1200px;
    height: 810px;
    overflow: hidden;
    background: var(--stage);
    font-family: "Questrial", "Helvetica Neue", Arial, sans-serif;
  }
  .stage { position: relative; width: 1200px; height: 810px; }

  .card {
    position: absolute;
    width: 520px;
    height: 336px;
    background: var(--card);
    border-radius: 22px;
    box-shadow: 0 10px 28px var(--shadow);
    overflow: hidden;
  }
  .card--front { left: 70px; top: 80px; }
  .card--back  { left: 610px; top: 394px; }

  .brand {
    position: absolute;
    display: flex;
    align-items: center;
    gap: 16px;
    color: var(--lime);
  }
  .brand__dot {
    width: 38px;
    height: 38px;
    border: 3px solid var(--lime);
    border-radius: 50%;
    flex: none;
  }
  .brand__name {
    font-size: 26px;
    letter-spacing: 0.42em;
    text-transform: uppercase;
    white-space: nowrap;
  }
  .card--front .brand { left: 50%; top: 50%; transform: translate(-50%, -50%); }
  .card--back .brand { left: 44px; top: 196px; }
  .card--back .brand__name { font-size: 20px; }
  .card--back .brand__dot { width: 30px; height: 30px; }

  .edge-band {
    position: absolute;
    width: 8px;
    background: var(--lime);
  }
  .edge-band--right { right: 0; top: 34px; height: 92px; border-radius: 4px 0 0 4px; }
  .edge-band--left  { left: 0; top: 212px; height: 92px; border-radius: 0 4px 4px 0; }

  .contact {
    position: absolute;
    right: 40px;
    top: 42px;
    text-align: right;
    color: var(--ink-light);
  }
  .contact__name { color: var(--lime); font-size: 22px; }
  .contact__role { font-size: 14px; margin-top: 2px; }
  .contact__list { list-style: none; margin-top: 22px; font-size: 15px; line-height: 1.7; }
  .contact__list li { display: flex; align-items: center; justify-content: flex-end; gap: 8px; }
  .contact__icon { width: 13px; height: 13px; fill: var(--lime); flex: none; }
</style>
</head>
<body>
<main class="stage">
  <section class="card card--front" aria-label="Card front">
    <div class="brand">
      <span class="brand__dot"></span>
      <span class="brand__name">Brio Margin</span>
    </div>
  </section>

  <section class="card card--back" aria-label="Card back">
    <span class="edge-band edge-band--right"></span>
    <span class="edge-band edge-band--left"></span>

    <div class="contact">
      <p class="contact__name">Dorian Palleck</p>
      <p class="contact__role">President</p>
      <ul class="contact__list">
        <li>0400123456
          <svg class="contact__icon" viewBox="0 0 24 24" aria-hidden="true"><path d="M6.6 10.8a15.1 15.1 0 0 0 6.6 6.6l2.2-2.2c.3-.3.7-.4 1-.2 1.1.4 2.3.6 3.6.6.6 0 1 .4 1 1V20c0 .6-.4 1-1 1A17 17 0 0 1 3 4c0-.6.4-1 1-1h3.5c.6 0 1 .4 1 1 0 1.3.2 2.5.6 3.6.1.3 0 .7-.2 1z"/></svg>
        </li>
        <li>hello@briomargin.com
          <svg class="contact__icon" viewBox="0 0 24 24" aria-hidden="true"><path d="M2 5h20v14H2z M4 7v.4l8 5 8-5V7l-8 5z" fill-rule="evenodd"/></svg>
        </li>
      </ul>
    </div>

    <div class="brand">
      <span class="brand__dot"></span>
      <span class="brand__name">Brio Margin</span>
    </div>
  </section>
</main>
</body>
</html>
```